Modern, Sleek Business Card Design for Corvane Systems

Please create a modern business card, preferably all black with white logo and writing for Corvane Systems, a defense and aerospace company.

Contact Information for Business Card

symbol on one side and name, title, contact info on the other side.

```html
<!DOCTYPE html>
<html lang="en">
<head>
<meta charset="utf-8">
<title>Corvane Systems – Business Card</title>
<link href="https://fonts.googleapis.com/css2?family=Montserrat:wght@400;700&display=swap" rel="stylesheet">
<style>
  :root {
    --backdrop: #2d2d2d;
    --card: #171717;
    --ink: #ffffff;
    --silver: #c9c9c9;
    --shade: #0c0c0c;
  }
  * { margin: 0; padding: 0; box-sizing: border-box; }
  html, body {
    width: 1200px; height: 1059px; overflow: hidden;
    background: var(--backdrop);
    font-family: 'Montserrat', sans-serif;
  }
  .card {
    position: absolute;
    width: 690px; height: 394px;
    background: var(--card);
    border-radius: 24px;
    overflow: hidden;
  }
  .card--front { left: 256px; top: 100px; }
  .card--back  { left: 253px; top: 536px; }

  .brand { position: absolute; display: flex; align-items: center; color: var(--ink); font-weight: 400; }
  .brand__square { background: var(--ink); flex: none; }
  .brand__name { line-height: 1; }
  .brand__main { display: block; letter-spacing: 0.08em; }
  .brand__sub { display: block; letter-spacing: 0.55em; text-align: right; }

  .card--front .brand { left: 28px; top: 26px; gap: 14px; }
  .card--front .brand__square { width: 44px; height: 44px; }
  .card--front .brand__main { font-size: 36px; }
  .card--front .brand__sub { font-size: 12px; margin-top: 6px; }

  .feature-block {
    position: absolute; left: 400px; top: 100px;
    width: 230px; height: 230px;
    background: linear-gradient(135deg, var(--shade) 0%, #1a1a1a 45%, var(--silver) 100%);
  }

  .identity { position: absolute; left: 0; top: 138px; padding-left: 28px; }
  .identity__bar { position: absolute; left: 0; top: 0; width: 15px; height: 55px; background: var(--ink); }
  .identity__name { color: var(--ink); font-weight: 700; font-size: 31px; line-height: 1; margin-top: 0; }
  .identity__title { color: var(--ink); font-size: 18px; margin-top: 6px; }

  .address { position: absolute; left: 28px; top: 218px; color: var(--ink); font-size: 18px; line-height: 27px; }

  .contacts { position: absolute; left: 26px; top: 264px; list-style: none; color: var(--ink); font-size: 18px; }
  .contacts li { display: flex; align-items: center; height: 27.5px; }
  .contacts svg { width: 14px; height: 14px; margin-right: 9px; fill: var(--ink); flex: none; }

  .card--back .brand { left: 70px; top: 140px; gap: 26px; color: var(--silver); }
  .card--back .brand__square { width: 96px; height: 96px; background: var(--silver); }
  .card--back .brand__main { font-size: 64px; }
  .card--back .brand__sub { font-size: 20px; margin-top: 14px; }
</style>
</head>
<body>
  <section class="card card--front">
    <div class="brand">
      <span class="brand__square"></span>
      <span class="brand__name">
        <span class="brand__main">CORVANE</span>
        <span class="brand__sub">SYSTEMS</span>
      </span>
    </div>

    <div class="feature-block" role="img" aria-label="Large brand symbol area"></div>

    <div class="identity">
      <span class="identity__bar"></span>
      <h1 class="identity__name">MARCUS HALE</h1>
      <p class="identity__title">Managing Director</p>
    </div>

    <p class="address">Your address, City<br>State, Zip 1234</p>

    <ul class="contacts">
      <li>
        <svg viewBox="0 0 16 16"><path d="M1 6c0-2 3-3 7-3s7 1 7 3v1h-4V5.5H5V7H1zM3 8h10l1 5H2z"/></svg>
        123 456 789
      </li>
      <li>
        <svg viewBox="0 0 16 16"><path d="M1 3h14v1.5L8 9 1 4.5zM1 6.3l7 4.5 7-4.5V13H1z"/></svg>
        info@corvanesystems.com
      </li>
      <li>
        <svg viewBox="0 0 16 16"><circle cx="8" cy="8" r="7"/><path d="M5 4l3 2-1 3 2 2-1 3M10 3l1 3 3 1" stroke="#171717" stroke-width="1.2" fill="none"/></svg>
        www.corvanesystems.com
      </li>
    </ul>
  </section>

  <section class="card card--back">
    <div class="brand">
      <span class="brand__square"></span>
      <span class="brand__name">
        <span class="brand__main">CORVANE</span>
        <span class="brand__sub">SYSTEMS</span>
      </span>
    </div>
  </section>
</body>
</html>
```